Industrial & commercial facility maintenance flyer

Design a 2 sided flyer that outlines our core business unit services. One side shall be for our industrial maintenance division while the other will be focused on our commercial maintenance division.

Media from website here: https://files.vornelbox.net/share/7Kq29XzPw4RtLmYc8NdHe5JbVa

Target Market(s)

Industrial and commercial facility maintenance companies and professionals

Industry/Entity Type

Maintenance

Font styles to use
Serif

Colors
ffffff
2f73b4
0455a3
cfdfed

Requirements
Must have
• Several photos of each applicable service. Reference existing website (www.trelcorp.com). Use of the blue and grey scheme of our current logo.
Nice to have
• Our logo design across the top with our contact information on the bottom.

```html
<!DOCTYPE html>
<html lang="en">
<head>
<meta charset="utf-8">
<title>Trelcorp Facility Services – Division Flyers</title>
<link rel="stylesheet" href="https://fonts.googleapis.com/css2?family=Oswald:wght@300;400;700&display=swap">
<style>
  :root {
    --backdrop: #61666b;
    --paper: #ffffff;
    --brand-blue: #0455a3;
    --accent-blue: #2f73b4;
    --pale-blue: #cfdfed;
    --ink: #222a33;
    --brand-grey: #55595e;
  }
  * { margin: 0; padding: 0; box-sizing: border-box; }
  html, body { width: 1200px; height: 1200px; overflow: hidden; }
  body { background: var(--backdrop); position: relative; font-family: "Oswald", sans-serif; }

  .flyer { position: absolute; top: 246px; height: 754px; background: var(--paper); overflow: hidden; }
  .flyer--industrial { left: 46px; width: 538px; }
  .flyer--commercial { left: 616px; width: 540px; }

  .photo { position: absolute; }

  .brand { position: absolute; display: flex; align-items: center; gap: 10px; }
  .brand__dot { width: 40px; height: 40px; border-radius: 50%; background: var(--brand-grey); flex: none; }
  .brand__name { font-weight: 400; font-size: 19px; color: var(--accent-blue); letter-spacing: 0.2px; line-height: 1; }

  .title { position: absolute; font-weight: 700; font-size: 37px; line-height: 40.5px; letter-spacing: 1.4px; color: var(--brand-blue); text-transform: uppercase; }
  .copy { position: absolute; font-weight: 300; font-size: 15px; line-height: 20.2px; color: var(--ink); }

  .contact-band { position: absolute; left: 0; right: 0; top: 650px; height: 76px; background: var(--brand-blue);
    display: flex; flex-direction: column; justify-content: center; align-items: center;
    color: var(--paper); font-weight: 300; font-size: 13px; line-height: 20px; text-align: center; }
  .contact-band strong { font-weight: 400; }
</style>
</head>
<body>

<section class="flyer flyer--industrial">
  <div class="photo" role="img" aria-label="Industrial plant with tanks and towers under a blue sky, framed by leaves" style="left:0;top:0;width:240px;height:292px;background:linear-gradient(180deg,#a9b8d8 0%,#c8c8cf 45%,#6f6a5a 75%,#4f6a36 100%);"></div>
  <div class="photo" role="img" aria-label="Factory floor machinery with yellow rails" style="left:0;top:304px;width:114px;height:146px;background:linear-gradient(160deg,#c9c8bd,#8b8a6e 60%,#6d6a55);"></div>
  <div class="photo" role="img" aria-label="Conveyor rollers in a large production hall" style="left:125px;top:304px;width:115px;height:146px;background:linear-gradient(170deg,#7e8690,#9a9a6e 55%,#5d6158);"></div>
  <div class="photo" role="img" aria-label="Stainless steel piping with blue valves and gauges" style="left:0;top:462px;width:240px;height:292px;background:linear-gradient(150deg,#d3d5d8,#9aa0a8 50%,#5c6470);"></div>

  <div class="brand" style="left:274px;top:78px;">
    <span class="brand__dot"></span>
    <span class="brand__name">Trelcorp Facility Services</span>
  </div>

  <h1 class="title" style="left:282px;top:164px;">Industrial<br>Maintenance<br>Solutions</h1>

  <p class="copy" style="left:280px;top:326px;width:226px;">Our industrial maintenance teams work in the field to handle your needs as quickly as possible, whether to get your critical broken or malfunctioning equipment going again or to support scheduled downtime. We specialize in industrial maintenance, conveyer repair, and overhead door repair, but our industrial services aren’t limited to those services. Others include equipment repairs, installation, and adjustment, just to name a few.</p>

  <div class="contact-band">
    <span>We greatly appreciate you taking the time to visit our website: <strong>www.trelcorp.com</strong></span>
    <span>We look forward to hearing from you! Office: 555 014 2380</span>
  </div>
</section>

<section class="flyer flyer--commercial">
  <div class="photo" role="img" aria-label="Worker with a hammer and tool pouch on his belt beside a wall" style="left:311px;top:0;width:229px;height:366px;background:linear-gradient(165deg,#b9b1a4,#8d7d6c 45%,#34363c 100%);"></div>
  <div class="photo" role="img" aria-label="Engine bay under an open car hood" style="left:311px;top:378px;width:70px;height:181px;background:linear-gradient(170deg,#5a7d95,#2a3d4f 60%,#1c2733);"></div>
  <div class="photo" role="img" aria-label="Hand tools, safety glasses and a red hard hat on a wooden bench" style="left:392px;top:378px;width:148px;height:181px;background:linear-gradient(150deg,#8c5a3c,#6e4430 60%,#a33a32);"></div>
  <div class="photo" role="img" aria-label="Technician in blue overalls standing by a service van" style="left:311px;top:570px;width:229px;height:184px;background:linear-gradient(180deg,#dfe2e4,#b9bcbf 50%,#2f4f94 100%);"></div>

  <div class="brand" style="left:34px;top:78px;">
    <span class="brand__dot"></span>
    <span class="brand__name">Trelcorp Facility Services</span>
  </div>

  <h1 class="title" style="left:35px;top:142px;">Retail &amp;<br>Commercial<br>Maintenance<br>Solutions</h1>

  <p class="copy" style="left:34px;top:356px;width:232px;">Trelcorp Facility Services knows how important it is to convert window shoppers to paying customers and to move inventory off your shelves. We ensure that your business is always looking its best with our cost-effective maintenance programs and crews available 24/7 to take care of any equipment or facility malfunction as quickly as possible.</p>

  <div class="contact-band">
    <span>We greatly appreciate you taking the time to visit our website: <strong>www.trelcorp.com</strong></span>
    <span>We look forward to hearing from you! Office: 555 014 2380</span>
  </div>
</section>

</body>
</html>
```